Brightvale LLC

This is for a flyer we will use to attract the bulk of our customers. We walk around the tourist area of San Francisco and look for people that want to go hiking in the Marin head lands.

Come with us on an amazing adventure just 30 minutes from San Francisco. We will guide you up this incredible mountain via the historic scenic railroad. This tour leaves from San Francisco at the end of Corliss Ave at Harbortide Green and takes you through scenic Mill Valley to the base of Mt Tam. From there we go on foot to the summit. This wonderful hike has many scenic over looks and endless opportunities for pictures. We climb at a comfortable pace and look for customers to be in good shape for climbing so every one can make it easily. It is not a technical climb and requires no special equipment or gear. For more info and to sign up for an unforgettable experience please visit our web site. Use Coupon code 585858 for 10% off.

Reason: Need to see more selection.

Target Market(s)

Europeans and fit Americans that want to climb a mountain in a couple of hours. People that want adventure and and are up for any thing. Check out our web site for more design cues. www.trekduvora.com.

Industry/Entity Type

Coupon

Requirements
Must have
• The California flag as the key design element. Should also have a mountain motif.
Should not have
• Heavy back packs. Camel packs only.

```html
<!DOCTYPE html>
<html lang="en">
<head>
<meta charset="utf-8">
<title>Brightvale LLC – Postcard</title>
<link href="https://fonts.googleapis.com/css2?family=Arvo:wght@400;700&family=Open+Sans:wght@400;600;700&family=Passion+One&family=Oswald:wght@600;700&display=swap" rel="stylesheet">
<style>
  :root{
    --page:#5a5a5a;
    --paper:#e9e8e3;
    --ink:#2f2f2f;
    --green:#13924a;
    --red:#b71f24;
    --teal-top:#4f9886;
    --night:#2a2a2a;
    --mint:#5ec38a;
    --white:#ffffff;
  }
  *{box-sizing:border-box;margin:0;padding:0}
  html,body{width:809px;height:1200px;overflow:hidden;background:var(--page)}
  body{position:relative;font-family:"Open Sans",sans-serif}

  .card{position:absolute;overflow:hidden}
  .card--front{left:53px;top:54px;width:684px;height:528px;background:var(--paper)}
  .card--back{left:53px;top:627px;width:692px;height:533px;background:var(--white)}

  /* front */
  .front__title{position:absolute;top:20px;left:0;width:100%;text-align:center;
    font-family:"Arvo",serif;font-weight:400;font-size:34px;color:var(--ink);letter-spacing:.5px;line-height:40px}
  .front__tagline{position:absolute;top:65px;left:124px;width:433px;height:20px;background:var(--green);
    color:var(--white);font-size:14.5px;line-height:20px;text-align:center;text-transform:uppercase;letter-spacing:.2px}
  .front__photo{position:absolute;left:73px;top:95px;width:531px;height:284px;border:4px solid var(--white);
    background:linear-gradient(180deg,#9ec3e4 0%,#cfdbe6 28%,#55706a 48%,#6c8ea6 62%,#3f4e45 78%,#b8b3a6 100%);
    box-shadow:0 2px 8px rgba(0,0,0,.35)}
  .front__band{position:absolute;left:0;top:296px;width:684px;height:232px}
  .front__lead{position:absolute;left:77px;top:372px;color:var(--white);font-weight:700;font-size:19px}
  .front__headline{position:absolute;left:74px;top:400px;color:var(--white);font-family:"Passion One",sans-serif;
    font-size:62px;letter-spacing:4px;line-height:1;white-space:nowrap}
  .front__strap{position:absolute;left:197px;top:474px;width:416px;height:23px;background:var(--white);
    color:var(--red);font-family:"Oswald",sans-serif;font-weight:600;font-size:15.5px;line-height:23px;
    letter-spacing:3.2px;text-align:center;text-transform:uppercase}

  /* back */
  .back__panel{position:absolute;left:0;top:0;width:420px;height:533px}
  .back__heading{position:absolute;left:20px;top:28px;width:136px;height:31px;background:var(--paper);
    color:var(--teal-top);font-family:"Oswald",sans-serif;font-weight:700;font-size:22px;line-height:31px;
    letter-spacing:4px;text-align:center}
  .back__copy{position:absolute;left:20px;top:71px;width:350px;color:var(--white);font-size:13.3px;line-height:16.6px}
  .back__coupon{position:absolute;left:58px;top:296px;width:216px;height:100px}
  .coupon__label{position:absolute;left:14px;top:32px;font-family:"Oswald",sans-serif;font-weight:700;font-size:16px;color:var(--night)}
  .coupon__code{position:absolute;left:13px;top:50px;font-family:"Oswald",sans-serif;font-weight:700;font-size:25px;color:var(--green)}
  .coupon__value{position:absolute;left:101px;top:24px;font-family:"Oswald",sans-serif;font-weight:700;font-size:52px;color:var(--red);line-height:1}
  .coupon__off{position:absolute;left:195px;top:33px;font-family:"Oswald",sans-serif;font-weight:600;font-size:13px;color:var(--red)}
  .back__info{position:absolute;left:0;top:455px;width:352px;text-align:center;color:var(--mint);font-size:13.5px;line-height:17px}
  .back__url{position:absolute;left:0;top:492px;width:352px;text-align:center;color:var(--white);font-weight:600;font-size:17px}
  .back__stamp{position:absolute;left:595px;top:91px;width:56px;height:66px;border:1.5px solid var(--night)}
  .back__line{position:absolute;left:427px;width:226px;height:1.5px;background:var(--night)}
</style>
</head>
<body>

<section class="card card--front">
  <h1 class="front__title">Trek Duvora</h1>
  <p class="front__tagline">Hike to the best view in San Francisco Bay Area</p>
  <div class="front__photo" role="img" aria-label="Hiker resting on a rocky summit overlooking a mountain lake and snowy peaks"></div>
  <svg class="front__band" viewBox="0 0 684 232" preserveAspectRatio="none" aria-hidden="true">
    <defs>
      <linearGradient id="bandRed" x1="0" y1="0" x2="0" y2="1">
        <stop offset="0" stop-color="#c2252a"/><stop offset="1" stop-color="#a81d21"/>
      </linearGradient>
    </defs>
    <path fill="#1b9a4e" d="M0 8 L40 2 L80 10 L120 6 L160 18 L200 14 L240 24 L280 20 L330 30 L370 26 L420 34 L470 36 L520 44 L570 48 L620 52 L684 58 L684 232 L0 232 Z"/>
    <path fill="url(#bandRed)" d="M0 18 L40 12 L80 20 L120 16 L160 28 L200 24 L240 34 L280 30 L330 40 L370 36 L420 44 L470 46 L520 54 L570 58 L620 62 L684 68 L684 232 L0 232 Z"/>
  </svg>
  <p class="front__lead">Come with us on an</p>
  <p class="front__headline">Amazing Adventure</p>
  <p class="front__strap">Just 30 minutes from San Francisco</p>
</section>

<section class="card card--back">
  <svg class="back__panel" viewBox="0 0 420 533" preserveAspectRatio="none" role="img" aria-label="Misty city skyline and hills in the lower part of the panel">
    <defs>
      <linearGradient id="panelTeal" x1="0" y1="0" x2="0" y2="1">
        <stop offset="0" stop-color="#4f9886"/><stop offset=".5" stop-color="#6a9d90"/><stop offset=".8" stop-color="#9fb7ae"/><stop offset="1" stop-color="#7f9c93"/>
      </linearGradient>
    </defs>
    <path fill="url(#panelTeal)" d="M0 0 L402 0 L396 40 L404 80 L392 130 L400 180 L388 230 L396 280 L384 330 L392 380 L380 430 L386 480 L376 533 L0 533 Z"/>
    <path fill="#2a2a2a" d="M0 440 L30 436 L60 442 L90 430 L120 438 L150 428 L180 440 L210 432 L240 442 L270 434 L300 444 L330 438 L360 446 L380 442 L376 533 L0 533 Z"/>
  </svg>
  <h2 class="back__heading">ABOUT US</h2>
  <p class="back__copy">We walk around the tourist area of San Francisco and look for people that want to go hiking in the Marin head lands. We will guide you up this incredible mountain via the historic scenic railroad. This tour leaves from San Francisco at the end of Corliss Ave at Harbortide Green and takes you through scenic Mill Valley to the base of Mt Tam. From there we go on foot to the summit. This wonderful hike has many scenic over looks and endless opportunities for pictures. We climb at a comfortable pace and look for customers to be in good shape for climbing so every one can make it easily. It is not a technical climb and requires no special equipment or gear.</p>

  <div class="back__coupon">
    <svg width="216" height="100" viewBox="0 0 216 100" aria-hidden="true">
      <defs>
        <linearGradient id="silver" x1="0" y1="0" x2="0" y2="1">
          <stop offset="0" stop-color="#ffffff"/><stop offset=".6" stop-color="#e4e4e4"/><stop offset="1" stop-color="#a9a9a9"/>
        </linearGradient>
      </defs>
      <path fill="url(#silver)" d="M14 6 Q108 -4 202 6 Q214 8 214 20 L214 80 Q214 92 202 94 Q108 104 14 94 Q2 92 2 80 L2 20 Q2 8 14 6 Z"/>
    </svg>
    <span class="coupon__label">Coupon code</span>
    <span class="coupon__code">585858</span>
    <span class="coupon__value">10%</span>
    <span class="coupon__off">off</span>
  </div>

  <p class="back__info">For more info and to sign up for an<br>unforgettable experience please visit</p>
  <p class="back__url">www.trekduvora.com</p>

  <div class="back__stamp"></div>
  <div class="back__line" style="top:303px"></div>
  <div class="back__line" style="top:338px"></div>
  <div class="back__line" style="top:375px"></div>
</section>

</body>
</html>
```